Brennick Holdings Business Cards

These are professional business cards that are for my family office.
Put fake emails and phone numbers as of now until I finalize those components. This family office controls my families investments, assets, and future. The cards should be professional.
..
.
.
.
I just uploaded another variation of a logo I would like to see as a business card to I am inbeteen which logo to use

Target Market(s)

business

Industry/Entity Type

business

Contact Information for Business Card

Professional, wealth related, finance related.

Requirements
Must have
• Logo

```html
<!DOCTYPE html>
<html lang="en">
<head>
<meta charset="utf-8">
<title>Brennick Holdings Business Cards</title>
<link rel="stylesheet" href="https://fonts.googleapis.com/css2?family=Cinzel:wght@400;600;700&family=Poppins:wght@400&display=swap">
<style>
  :root {
    --backdrop: #d1d2d4;
    --navy: #181e2b;
    --paper: #ffffff;
    --muted: #a7a9ac;
    --icon: #9b9da0;
  }
  html, body {
    margin: 0;
    padding: 0;
    width: 1200px;
    height: 859px;
    overflow: hidden;
    background: var(--backdrop);
  }
  .canvas {
    position: relative;
    width: 1200px;
    height: 859px;
  }
  .card {
    position: absolute;
    overflow: hidden;
  }
  .card svg.decor {
    position: absolute;
    left: 0;
    top: 0;
  }
  .card-front {
    left: 237px;
    top: 102px;
    width: 516px;
    height: 293px;
    background: var(--navy);
  }
  .card-back {
    left: 413px;
    top: 428px;
    width: 515px;
    height: 294px;
    background: var(--paper);
  }
  .brand {
    position: absolute;
    display: flex;
    flex-direction: column;
    align-items: center;
    transform: translateX(-50%);
  }
  .brand-mark {
    display: block;
    box-sizing: border-box;
    border-radius: 50%;
    border: 2px solid currentColor;
  }
  .brand-name {
    font-family: "Cinzel", serif;
    font-weight: 600;
    font-size: 15px;
    letter-spacing: 0.3px;
    white-space: nowrap;
    line-height: 1;
  }
  .card-front .brand {
    left: 113px;
    top: 144px;
    color: var(--paper);
  }
  .card-front .brand-mark {
    width: 82px;
    height: 82px;
    margin-bottom: 14px;
  }
  .card-back .brand {
    left: 420px;
    top: 25px;
    color: var(--navy);
  }
  .card-back .brand-mark {
    width: 76px;
    height: 76px;
    margin-bottom: 12px;
  }
  .holder {
    position: absolute;
    left: 23px;
    top: 130px;
  }
  .holder-name {
    margin: 0;
    font-family: "Cinzel", serif;
    font-weight: 700;
    font-size: 25px;
    line-height: 1;
    color: var(--navy);
    white-space: nowrap;
  }
  .holder-title {
    margin: 2px 0 0;
    font-family: "Cinzel", serif;
    font-weight: 400;
    font-size: 12px;
    letter-spacing: 0.8px;
    line-height: 1;
    color: var(--muted);
  }
  .contact-list {
    position: absolute;
    left: 23px;
    top: 224px;
    margin: 0;
    padding: 0;
    list-style: none;
    font-family: "Poppins", sans-serif;
    font-size: 13.5px;
    color: var(--navy);
  }
  .contact-list li {
    display: flex;
    align-items: center;
    height: 23px;
  }
  .contact-list svg {
    width: 14px;
    height: 14px;
    margin-right: 15px;
    fill: var(--icon);
  }
</style>
</head>
<body>
<main class="canvas">

  <section class="card card-front" aria-label="Business card front">
    <svg class="decor" width="516" height="293" viewBox="0 0 516 293" aria-hidden="true">
      <circle cx="437" cy="65" r="160" fill="none" stroke="var(--paper)" stroke-width="5"/>
    </svg>
    <div class="brand">
      <span class="brand-mark"></span>
      <span class="brand-name">Brennick Holdings</span>
    </div>
  </section>

  <section class="card card-back" aria-label="Business card back">
    <svg class="decor" width="515" height="294" viewBox="0 0 515 294" aria-hidden="true">
      <circle cx="99" cy="217" r="160" fill="none" stroke="var(--navy)" stroke-width="8"/>
    </svg>
    <div class="brand">
      <span class="brand-mark"></span>
      <span class="brand-name">Brennick Holdings</span>
    </div>
    <div class="holder">
      <h1 class="holder-name">ANNA REED</h1>
      <p class="holder-title">DESIGNATION</p>
    </div>
    <ul class="contact-list">
      <li>
        <svg viewBox="0 0 24 24" aria-hidden="true"><path d="M6.6 10.8a15.1 15.1 0 0 0 6.6 6.6l2.2-2.2c.3-.3.7-.4 1-.2 1.1.4 2.3.6 3.6.6.6 0 1 .4 1 1V20c0 .6-.4 1-1 1A17 17 0 0 1 3 4c0-.6.4-1 1-1h3.5c.6 0 1 .4 1 1 0 1.3.2 2.5.6 3.6.1.3 0 .7-.2 1l-2.3 2.2z"/></svg>
        <span>123.456.7890</span>
      </li>
      <li>
        <svg viewBox="0 0 24 24" aria-hidden="true"><path d="M2 5h20v14H2V5zm2 2v.5l8 5 8-5V7H4zm16 2.8-8 5-8-5V17h16V9.8z"/></svg>
        <span>office@brennick.example</span>
      </li>
    </ul>
  </section>

</main>
</body>
</html>
```